IT Consulting Business needs a web design

We need a web design for an IT Consulting company called "Verunex". We want to replace the existing web site (www.verunex-example.com) with a new design. Our services are IT Consulting, IT Training, IT Outsourcing.
We would like to see designs that communicate "Trusted IT Advisor" with modern & bold design.

We would like to see the design of 2 pages:
1. Home page (www.verunex-example.com)
2. The detail page (http://www.verunex-example.com/index_files/consulting.htm)

```html
<!DOCTYPE html>
<html lang="en">
<head>
<meta charset="utf-8">
<title>Verunex – Trusted IT Advisor</title>
<link href="https://fonts.googleapis.com/css2?family=PT+Sans:ital,wght@0,400;0,700;1,400;1,700&display=swap" rel="stylesheet">
<style>
  :root {
    --brand-blue: #2a7fd0;
    --nav-top: #3d8ee0;
    --nav-bottom: #1a5fae;
    --nav-edge: #0f3f78;
    --hero-deep: #03112e;
    --hero-mid: #0b3a78;
    --hero-warm: #8a6a4e;
    --consult: #e8734a;
    --consult-dark: #c4532f;
    --train: #e7b535;
    --train-dark: #c8921a;
    --solve: #1fbac8;
    --solve-dark: #12919c;
    --ink: #222;
    --rule: #e2e2e2;
    --white: #fff;
  }
  * { box-sizing: border-box; margin: 0; padding: 0; }
  html, body { width: 891px; height: 1200px; overflow: hidden; background: var(--white); }
  .page { position: relative; width: 891px; height: 1200px; font-family: Arial, Helvetica, sans-serif; color: var(--ink); }

  .site-header { position: absolute; left: 0; top: 0; width: 891px; height: 72px; }
  .brand { position: absolute; left: 14px; top: 18px; display: flex; align-items: center; gap: 8px;
    font-family: "PT Sans", sans-serif; font-weight: 700; font-size: 30px; letter-spacing: 2px; color: var(--brand-blue); }
  .brand-mark { width: 14px; height: 14px; background: var(--consult); border-radius: 50%; }
  .address { position: absolute; right: 9px; top: 5px; text-align: right; font-family: "PT Sans", sans-serif;
    font-style: italic; font-weight: 700; font-size: 10.5px; line-height: 13px; color: #666; }
  .phone { position: absolute; right: 9px; top: 36px; font-family: "PT Sans", sans-serif; font-style: italic;
    font-weight: 700; font-size: 27px; color: #b8bcc2; letter-spacing: 0.5px; }

  .main-nav { position: absolute; left: 0; top: 72px; width: 891px; height: 53px;
    background: linear-gradient(var(--nav-top), var(--nav-bottom)); border-top: 1px solid var(--nav-edge); border-bottom: 3px solid var(--nav-edge); }
  .main-nav a { position: absolute; top: 16px; font-family: "PT Sans", sans-serif; font-style: italic; font-weight: 700;
    font-size: 14px; color: var(--white); text-decoration: none; }
  .nav-sep { position: absolute; top: 6px; width: 1px; height: 40px; background: rgba(255,255,255,0.35); transform: skewX(-12deg); }

  .hero { position: absolute; left: 0; top: 125px; width: 891px; height: 301px;
    background: radial-gradient(ellipse at 68% 45%, var(--hero-warm) 0%, #3a3a4a 28%, transparent 55%),
                linear-gradient(90deg, var(--hero-deep) 0%, var(--hero-mid) 35%, #0d2a55 60%, #1a1a24 100%); overflow: hidden; }
  .tag { position: absolute; font-family: "PT Sans", sans-serif; font-style: italic; font-weight: 700; color: #dfe9f5;
    border: 1px solid rgba(200,220,255,0.7); border-right: none; border-radius: 6px 0 0 6px; padding: 1px 6px; }
  .tag-lg { font-size: 15px; }
  .tag-sm { font-size: 9px; }
  .hero-title { position: absolute; left: 228px; top: 80px; font-family: "PT Sans", sans-serif; font-style: italic;
    font-weight: 700; font-size: 27px; color: #e8f2ff; text-shadow: 0 0 10px rgba(120,180,255,0.8); }

  .services { position: absolute; left: 89px; top: 392px; width: 743px; height: 352px; background: var(--white); }
  .card { position: absolute; top: 9px; width: 230px; height: 332px; color: var(--white); }
  .card-image { width: 100%; height: 132px; }
  .card-body { height: 200px; padding: 15px 18px 0 13px; border-top: 3px solid rgba(0,0,0,0.08); }
  .card h2 { font-family: "PT Sans", sans-serif; font-style: italic; font-weight: 400; font-size: 22px; margin-bottom: 6px; }
  .card p { font-size: 10px; line-height: 12.5px; padding-left: 2px; }
  .more { position: absolute; left: 22px; bottom: 34px; width: 51px; height: 28px; font-size: 8px; font-weight: 700;
    display: flex; align-items: center; justify-content: center; color: var(--white); text-decoration: none; }
  .card-consult { left: 11px; }
  .card-consult .card-image { background: linear-gradient(135deg, #e4e6ea, #9aa3ad 60%, #1e9fe0); }
  .card-consult .card-body { background: linear-gradient(var(--consult), #e66843); }
  .card-consult .more { background: var(--consult-dark); }
  .card-train { left: 256px; }
  .card-train .card-image { background: linear-gradient(180deg, #1c2a44, #0d4c8a 45%, #e9ecef 85%); }
  .card-train .card-body { background: linear-gradient(var(--train), #e2ac2d); }
  .card-train .more { background: var(--train-dark); }
  .card-solve { left: 503px; }
  .card-solve .card-image { background: linear-gradient(135deg, #0a2d7a, #1f64c8 55%, #8fb8ee); }
  .card-solve .card-body { background: linear-gradient(var(--solve), #19b0bd); }
  .card-solve .more { background: var(--solve-dark); }

  .intro { position: absolute; left: 41px; top: 766px; width: 830px; font-size: 12px; line-height: 14px; }
  .intro p + p { margin-top: 13px; }

  .partner-name { position: absolute; left: 52px; top: 898px; font-family: "PT Sans", sans-serif; font-weight: 700;
    font-size: 34px; color: #1e1e1e; letter-spacing: -1px; }
  .growth-art { position: absolute; left: 50px; top: 948px; width: 155px; height: 105px;
    background: radial-gradient(ellipse at 55% 60%, #cfd6dc 0%, #eef0f2 55%, #ffffff 85%); border-radius: 6px; }
  .screens { position: absolute; left: 285px; top: 892px; width: 152px; height: 155px;
    background: linear-gradient(180deg, #2a2a2a, #4d6a8a 50%, #d8d8d8); border-radius: 4px; opacity: 0.9; }
  .focus { position: absolute; left: 473px; top: 908px; font-size: 12px; }
  .focus h3 { font-size: 12px; font-weight: 700; margin-bottom: 14px; }
  .focus ul { list-style: none; padding-left: 16px; line-height: 13.6px; }
  .focus li::before { content: "· "; }

  .footer-nav { position: absolute; left: 0; top: 1129px; width: 891px; height: 29px; border-top: 1px solid var(--rule);
    border-bottom: 1px solid var(--rule); text-align: center; font-family: "PT Sans", sans-serif; font-size: 13.5px; line-height: 27px; color: #333; }
  .footer-nav a { color: #333; text-decoration: none; }
  .copyright { position: absolute; left: 0; top: 1171px; width: 891px; text-align: center; font-family: "PT Sans", sans-serif;
    font-size: 10.5px; color: #8a8a8a; }
</style>
</head>
<body>
<div class="page">
  <header class="site-header">
    <div class="brand"><span>Verunex</span><span class="brand-mark"></span></div>
    <div class="address">88/14 Lorvan Lane 7, Fenmoor Rd., Ashdale,<br>Kelvar 20480 Nordania</div>
    <div class="phone">PHONE: 02-555-0188</div>
  </header>

  <nav class="main-nav">
    <a href="#" style="left:23px">HOME</a>
    <span class="nav-sep" style="left:90px"></span>
    <a href="#" style="left:115px">OUR VALUE</a>
    <span class="nav-sep" style="left:211px"></span>
    <a href="#" style="left:240px">OUR SERVICES</a>
    <span class="nav-sep" style="left:358px"></span>
    <a href="#" style="left:383px">OUR EXPERTISE</a>
    <span class="nav-sep" style="left:503px"></span>
    <a href="#" style="left:535px">JOBS</a>
    <span class="nav-sep" style="left:598px"></span>
    <a href="#" style="left:622px">CONTACT US</a>
  </nav>

  <section class="hero" role="img" aria-label="Photo of a woman touching a glowing digital interface grid">
    <span class="tag tag-lg" style="left:40px;top:24px">BUSINESS SOLUTIONS</span>
    <span class="tag tag-sm" style="left:241px;top:55px">COLLABORATION</span>
    <span class="hero-title">TRUSTED IT ADVISOR</span>
    <span class="tag tag-lg" style="left:98px;top:131px">DOCUMENT MANAGEMENT</span>
    <span class="tag tag-lg" style="left:358px;top:171px;font-size:18px">ROI</span>
    <span class="tag tag-lg" style="left:47px;top:200px">WEB</span>
  </section>

  <section class="services">
    <article class="card card-consult">
      <div class="card-image" role="img" aria-label="Blue puzzle piece fitting into grey puzzle"></div>
      <div class="card-body">
        <h2>consulting</h2>
        <p>Our experienced, certified professionals provides IT consulting using industry recommended practices. We are specialized in Norvale Business Productivity Platform.</p>
      </div>
      <a class="more" href="#">MORE</a>
    </article>
    <article class="card card-train">
      <div class="card-image" role="img" aria-label="Computer monitors showing a world map"></div>
      <div class="card-body">
        <h2>training</h2>
        <p>Our certified trainers provide in-house training for Verunex original courses as well as customized training courses that suit your organization needs.</p>
      </div>
      <a class="more" href="#">MORE</a>
    </article>
    <article class="card card-solve">
      <div class="card-image" role="img" aria-label="Network cable plug on a blue digital background"></div>
      <div class="card-body">
        <h2>solutions</h2>
        <p>Our unique solution services offer customers with the benefits of our expert consultants in designing, deploying, and implementing our solutions.</p>
      </div>
      <a class="more" href="#">MORE</a>
    </article>
  </section>

  <section class="intro">
    <p>We are experienced, certified professionals who are experts at Information Technology (IT) consulting, solution design &amp; development, and training for medium-size businesses and large enterprises.</p>
    <p>We are committed to helping our clients quickly achieve the most appropriate solution with sustainable ROI. We are focusing on Norvale Technologies for large organizations. We offer the agility of a smaller firm, the quality of larger firms.</p>
  </section>

  <section class="expertise">
    <div class="partner-name">Norvale</div>
    <div class="growth-art" role="img" aria-label="Illustration of a rising bar chart with a green arrow on report papers"></div>
    <div class="screens" role="img" aria-label="Curved display of website page layouts"></div>
    <div class="focus">
      <h3>Verunex specializes in Norvale technologies in the following areas:</h3>
      <ul>
        <li>Corporate intranet portal and public web site</li>
        <li>Business intelligence solution</li>
        <li>Enterprise search solution</li>
        <li>Document and record management solution</li>
        <li>Business form and enterprise collaboration solution</li>
        <li>Knowledge management solution</li>
      </ul>
    </div>
  </section>

  <footer>
    <nav class="footer-nav">
      <a href="#">home</a> · <a href="#">our value</a> · <a href="#">our services</a> · <a href="#">expertise</a> · <a href="#">jobs</a> · <a href="#">contact us</a>
    </nav>
    <p class="copyright">© Copyright 2010-2013 VERUNEX. All Rights Reserved.</p>
  </footer>
</div>
</body>
</html>
```